Redesign Business Cards, Attached

Please read instructions carefully. If you have any questions send a message before submitting your ONE design. Please redesign attached business cards. Double sided. Use same content and descriptions. Use black, silver, crimson red and gold colors. My only issue with the attached design is the background colors. I like the layout as-is. I can provide the individual pictures on the back side later. Do not submit more than one design. One submission shall include both front and back. Do not submit front and back separately. A second project will be launched to create a matching post card after completion of this.
Industry/Entity Type
see description and attachments.
Contact Information for Business Card
Requirements
Must have
- see description and attachments.
Nice to have
Should not have

```html
<!DOCTYPE html>
<html lang="en">
<head>
<meta charset="utf-8">
<title>Harbor Helm – Business Card, Front and Back</title>
<link href="https://fonts.googleapis.com/css2?family=Montserrat:ital,wght@0,300;0,400;0,600;0,700;1,600;1,700&display=swap" rel="stylesheet">
<style>
  :root {
    --backdrop: #9d9d9e;
    --crimson: #b3141f;
    --crimson-deep: #8e0d17;
    --gold: #d4af37;
    --gold-light: #e8cc6a;
    --gold-deep: #a8842a;
    --silver: #c9ccd1;
    --silver-light: #eceef1;
    --silver-deep: #8d9198;
    --black: #111111;
    --charcoal: #1e1f22;
    --white: #ffffff;
  }
  * { box-sizing: border-box; margin: 0; padding: 0; }
  html, body {
    width: 1200px; height: 1200px; overflow: hidden;
    background: var(--backdrop);
    font-family: "Montserrat", sans-serif;
  }
  .card {
    position: absolute; left: 166px; width: 868px; height: 507px;
    overflow: hidden; color: var(--white);
  }
  .card--front { top: 69px; }
  .card--back { top: 625px; }

  /* Front */
  .front-photo {
    position: absolute; inset: 0;
    background:
      radial-gradient(ellipse at 66% 58%, rgba(17,17,17,.55) 0%, rgba(17,17,17,0) 45%),
      linear-gradient(160deg, var(--gold-light) 0%, var(--gold) 40%, var(--gold-deep) 68%, var(--charcoal) 100%);
  }
  .front-chevron { position: absolute; inset: 0; width: 868px; height: 507px; }
  .holder { position: absolute; left: 59px; top: 95px; }
  .holder__name { font-size: 37px; font-weight: 600; line-height: 1.15; }
  .holder__role { font-size: 22px; font-weight: 300; line-height: 1.28; }
  .contacts { position: absolute; left: 59px; top: 286px; list-style: none; }
  .contacts li {
    display: flex; align-items: center; gap: 18px;
    font-size: 22px; font-weight: 300; height: 34px;
  }
  .contacts svg { width: 16px; height: 16px; flex: none; fill: var(--white); }

  .brand-seal {
    position: absolute; border-radius: 50%;
    display: flex; align-items: center; justify-content: center; text-align: center;
  }
  .brand-seal--front {
    left: 603px; top: 132px; width: 200px; height: 200px;
    background: var(--black);
  }
  .brand-seal__name {
    font-weight: 700; font-size: 22px; line-height: 1.2; letter-spacing: 1px;
    color: var(--gold); text-transform: uppercase;
  }

  /* Back */
  .back-photo {
    position: absolute; inset: 0;
    background:
      radial-gradient(ellipse at 76% 62%, var(--silver-light) 0%, rgba(236,238,241,0) 40%),
      linear-gradient(180deg, var(--silver) 0%, var(--silver-deep) 55%, var(--charcoal) 82%, var(--black) 100%);
  }
  .back-panel {
    position: absolute; left: 0; top: 0; width: 740px; height: 394px;
    background: linear-gradient(135deg, var(--gold-light) 0%, var(--gold) 45%, var(--gold-deep) 100%);
  }
  .back-band {
    position: absolute; left: 0; top: 394px; width: 868px; height: 113px;
    background: linear-gradient(90deg, var(--black) 0%, var(--charcoal) 60%, rgba(30,31,34,.6) 100%);
  }
  .services {
    position: absolute; left: 50px; top: 64px; list-style: none;
  }
  .services li {
    font-size: 19.5px; font-weight: 700; font-style: italic;
    line-height: 33.2px; color: var(--white);
    text-shadow: 0 1px 2px rgba(0,0,0,.25);
  }
  .brand-seal--back {
    left: 540px; top: 54px; width: 312px; height: 312px;
    background: var(--white);
    box-shadow: 0 0 0 6px var(--silver);
  }
  .brand-seal--back .brand-seal__inner {
    width: 240px; height: 240px; border-radius: 50%;
    background: var(--black);
    display: flex; align-items: center; justify-content: center;
  }
  .brand-seal--back .brand-seal__name { color: var(--gold); font-size: 26px; }
  .back-url {
    position: absolute; left: 111px; top: 428px;
    font-size: 25px; font-weight: 600; color: var(--silver-light);
  }
</style>
</head>
<body>

<section class="card card--front">
  <div class="front-photo" role="img" aria-label="Aerial photo of a motor boat cruising across gold-toned water"></div>
  <svg class="front-chevron" viewBox="0 0 868 507" aria-hidden="true">
    <defs>
      <linearGradient id="crimsonFill" x1="0" y1="0" x2="1" y2="1">
        <stop offset="0" stop-color="#c01826"/>
        <stop offset="1" stop-color="#8e0d17"/>
      </linearGradient>
    </defs>
    <polygon points="0,0 384,0 519,250 384,507 0,507" fill="url(#crimsonFill)"/>
  </svg>

  <div class="holder">
    <h1 class="holder__name">Jordan T. Halvers</h1>
    <p class="holder__role">USCG Licensed Captain</p>
    <p class="holder__role">Certified Instructor</p>
  </div>

  <ul class="contacts">
    <li>
      <svg viewBox="0 0 24 24"><path d="M6.6 10.8a15.1 15.1 0 0 0 6.6 6.6l2.2-2.2c.3-.3.7-.4 1-.2 1.1.4 2.3.6 3.6.6.6 0 1 .4 1 1V20c0 .6-.4 1-1 1A17 17 0 0 1 3 4c0-.6.4-1 1-1h3.5c.6 0 1 .4 1 1 0 1.3.2 2.5.6 3.6.1.3 0 .7-.2 1z"/></svg>
      (555) 014-2280
    </li>
    <li>
      <svg viewBox="0 0 24 24"><path d="M3 5h18a1 1 0 0 1 1 1v12a1 1 0 0 1-1 1H3a1 1 0 0 1-1-1V6a1 1 0 0 1 1-1zm9 7.5L20 7H4z"/></svg>
      hello@harborhelm.com
    </li>
    <li>
      <svg viewBox="0 0 24 24"><circle cx="12" cy="12" r="10"/><path d="M2 12h20M12 2c3 3 3 17 0 20M12 2c-3 3-3 17 0 20" stroke="#a8121d" stroke-width="1.6" fill="none"/></svg>
      www.HarborHelm.com
    </li>
  </ul>

  <div class="brand-seal brand-seal--front">
    <span class="brand-seal__name">Harbor<br>Helm</span>
  </div>
</section>

<section class="card card--back">
  <div class="back-photo" role="img" aria-label="Aerial photo of a motor boat on sunlit silver water"></div>
  <div class="back-panel"></div>
  <div class="back-band"></div>

  <ul class="services">
    <li>» Hands-on Boat Training</li>
    <li>» Introduction to Power Boating</li>
    <li>» Precision Docking &amp; Boat Handling</li>
    <li>» Open Water Boat Handling</li>
    <li>» Island Anchoring</li>
    <li>» Open Water Advanced Maneuvers</li>
    <li>» Coastal Navigation</li>
    <li>» Captaining / Piloting Service for Your Outings</li>
  </ul>

  <div class="brand-seal brand-seal--back">
    <div class="brand-seal__inner">
      <span class="brand-seal__name">Harbor<br>Helm</span>
    </div>
  </div>

  <p class="back-url">www.HarborHelm.com</p>
</section>

</body>
</html>
```